Need a sleek, professional business card design for a Web Development business

I need a unique business card designed for a web development company. It is also the parent company for any ventures I do, such as my ClipWave channel, startup ideas I have, etc. I am the single member of "Bright Harbor Code LLC." I will attach my basic logo here, so you will see the current color scheme and have the asset available. Thank you!

Target Market(s)

Startups, SMB's, Professionals

Industry/Entity Type

Business

Font styles to use
Other font styles liked:
• Lovello for headings is what I use, but not necessary.

Colors

Designer to choose colors to be used in the design.

Requirements
Nice to have
• Sleek is the word. Professional, modern, dark.
Should not have
• Any work from someone else's design. Lacking originality.

```html
<!DOCTYPE html>
<html lang="en">
<head>
<meta charset="utf-8">
<title>Bright Harbor Code LLC – Business Card</title>
<link href="https://fonts.googleapis.com/css2?family=Roboto:wght@400;500&family=Roboto+Condensed:wght@700&display=swap" rel="stylesheet">
<style>
  :root {
    --backdrop: #d8ae84;
    --card-white: #f4f4f4;
    --grad-center: #f99b63;
    --grad-edge: #ee5c6c;
    --ink: #222222;
    --ink-soft: #555555;
    --accent: #ef5a65;
  }
  * { margin: 0; padding: 0; box-sizing: border-box; }
  html, body { width: 1200px; height: 960px; overflow: hidden; }
  body {
    background: var(--backdrop);
    font-family: "Roboto", Arial, sans-serif;
    position: relative;
  }
  .card {
    position: absolute;
    left: 320px;
    width: 600px;
    height: 345px;
    border-radius: 22px;
    box-shadow: 0 3px 6px rgba(0,0,0,0.25);
  }
  .card-front {
    top: 103px;
    background: radial-gradient(ellipse at 50% 45%, var(--grad-center) 0%, var(--grad-edge) 100%);
  }
  .front-brand {
    position: absolute;
    top: 150px;
    left: 0;
    width: 100%;
    text-align: center;
    font-weight: 500;
    font-size: 36px;
    color: var(--ink);
  }
  .front-web {
    position: absolute;
    top: 294px;
    left: 0;
    width: 100%;
    text-align: center;
    font-size: 14px;
    letter-spacing: 5px;
    color: var(--ink);
  }
  .card-back {
    top: 492px;
    height: 343px;
    background: var(--card-white);
  }
  .contact-block {
    position: absolute;
    left: 32px;
    top: 124px;
  }
  .person-name {
    font-size: 21px;
    font-weight: 500;
    color: var(--accent);
    line-height: 26px;
  }
  .person-title {
    font-size: 15px;
    color: var(--ink);
    line-height: 20px;
    margin-bottom: 5px;
  }
  .address {
    font-size: 14px;
    color: var(--ink-soft);
    line-height: 18px;
    margin-bottom: 9px;
  }
  .contact-list { list-style: none; }
  .contact-list li {
    font-size: 14px;
    color: var(--ink-soft);
    line-height: 19px;
    display: flex;
    align-items: center;
  }
  .contact-list svg {
    width: 13px;
    height: 13px;
    margin-right: 10px;
    fill: var(--accent);
  }
  .brand-square {
    position: absolute;
    left: 406px;
    top: 31px;
    width: 159px;
    height: 159px;
    border-radius: 8px;
    background: var(--ink);
  }
  .brand-name {
    position: absolute;
    left: 356px;
    top: 195px;
    width: 260px;
    text-align: center;
    font-family: "Roboto Condensed", "Arial Narrow", sans-serif;
    font-weight: 700;
    font-size: 18px;
    color: var(--ink);
  }
</style>
</head>
<body>
  <section class="card card-front">
    <p class="front-brand">Bright Harbor Code LLC</p>
    <p class="front-web">www.brightharbor.dev</p>
  </section>

  <section class="card card-back">
    <div class="contact-block">
      <p class="person-name">EVAN MARLOW</p>
      <p class="person-title">CEO/FOUNDER</p>
      <p class="address">2194 Larkspur Court<br>Juneau, Alaska 99801</p>
      <ul class="contact-list">
        <li><svg viewBox="0 0 16 16"><path d="M3 1l3 3-2 2c1 2 3 4 6 6l2-2 3 3-2 2C7 15 1 9 1 3z"/></svg>555 214 3876</li>
        <li><svg viewBox="0 0 16 16"><path d="M4 0h8a1 1 0 011 1v14a1 1 0 01-1 1H4a1 1 0 01-1-1V1a1 1 0 011-1zm1 2v10h6V2zm3 11a1 1 0 100 2 1 1 0 000-2z"/></svg>555 730 1492</li>
        <li><svg viewBox="0 0 16 16"><path d="M4 1h8v4H4zM1 6h14v7h-3v2H4v-2H1zm4 5v3h6v-3z"/></svg>555 608 2251</li>
        <li><svg viewBox="0 0 16 16"><path d="M1 3h14v10H1zm1 1l6 5 6-5z"/></svg>evan@brightharbor.dev</li>
        <li><svg viewBox="0 0 16 16"><circle cx="8" cy="8" r="7"/></svg>www.brightharbor.dev</li>
      </ul>
    </div>
    <div class="brand-square"></div>
    <p class="brand-name">Bright Harbor Code LLC.</p>
  </section>
</body>
</html>
```